School Poster

Design so that these can be placed in classrooms across the school.

Attached is another design we have had done. Use a similar theme.

Consider using themes from https://tolvanehs.qx.edu.au/

please edit Binder1 doc.

Target Market(s)

Students and teachers

```html
<!DOCTYPE html>
<html lang="en">
<head>
<meta charset="utf-8">
<title>Before You Ask the Teacher – Tolvane State High School</title>
<link rel="stylesheet" href="https://fonts.googleapis.com/css2?family=Arimo:wght@700&family=Barlow+Condensed:ital,wght@1,800&family=Bebas+Neue&family=Montserrat:wght@500&family=Poppins:wght@600;700;800&display=swap">
<style>
  :root {
    --navy: #0f3f80;
    --yellow: #f6e87c;
    --check: #f3dd55;
    --card: #f6f6f6;
    --note: #e3e3e3;
    --photo-a: #bcc0c1;
    --photo-b: #aab0b2;
    --ink: #2a2a2a;
    --stage: #939393;
    --white: #ffffff;
  }
  * { box-sizing: border-box; margin: 0; padding: 0; }
  html, body { width: 1200px; height: 1200px; overflow: hidden; background: var(--stage); }

  .poster {
    position: absolute; left: 190px; top: 20px;
    width: 1000px; height: 1415px;
    transform: scale(0.82); transform-origin: 0 0;
    background: var(--navy);
    overflow: hidden;
  }

  .hero-art { position: absolute; left: 0; top: 0; width: 1000px; height: 600px; }

  .brand { position: absolute; left: 58px; top: 48px; display: flex; align-items: center; gap: 24px; }
  .brand-dot { width: 96px; height: 96px; border-radius: 50%; background: var(--yellow); flex: none; }
  .brand-name {
    font-family: "Arimo", Arial, sans-serif; font-weight: 700;
    font-size: 47px; line-height: 47px; color: var(--white);
  }
  .rule-top { position: absolute; left: 175px; top: 183px; width: 525px; height: 14px; background: var(--yellow); }

  .headline {
    position: absolute; left: 72px; top: 218px;
    font-family: "Barlow Condensed", "Arial Narrow", sans-serif;
    font-style: italic; font-weight: 800;
    font-size: 118px; line-height: 96px; letter-spacing: 1px;
    color: var(--white); text-transform: uppercase;
  }
  .headline .accent { color: var(--yellow); }
  .rule-mid { position: absolute; left: 0; top: 524px; width: 450px; height: 12px; background: var(--yellow); clip-path: polygon(0 0, 100% 0, 97% 100%, 0 100%); }

  .steps-banner {
    position: absolute; left: 42px; top: 548px; width: 724px; height: 68px;
    background: var(--yellow);
    clip-path: polygon(2.5% 0, 100% 0, 97.5% 100%, 0 100%);
    font-family: "Poppins", sans-serif; font-weight: 800;
    font-size: 51px; line-height: 72px; color: var(--navy);
    padding-left: 48px; letter-spacing: 0.5px;
  }

  .steps { position: absolute; left: 34px; top: 640px; display: flex; gap: 22px; }
  .step {
    position: relative; width: 296px; height: 592px;
    display: flex; flex-direction: column;
    border-radius: 0 30px 30px 0; background: var(--card);
  }
  .step-num {
    position: absolute; left: -14px; top: -16px; width: 46px; height: 46px;
    border-radius: 50%; background: var(--white); border: 3px solid var(--navy);
    font-family: "Poppins", sans-serif; font-weight: 800; font-size: 26px;
    line-height: 40px; text-align: center; color: var(--navy); z-index: 2;
  }
  .step-head {
    height: 123px; background: var(--yellow); border-radius: 0 30px 0 0;
    display: flex; align-items: center; padding-left: 34px;
  }
  .step-think .step-head { padding-left: 62px; }
  .step-icon { width: 58px; height: 58px; flex: none; }
  .step-divider { width: 2px; height: 94px; background: var(--navy); margin: 0 12px 0 18px; flex: none; }
  .step-title {
    font-family: "Bebas Neue", "Arial Narrow", sans-serif; font-weight: 400;
    font-size: 44px; line-height: 38px; color: var(--navy); text-transform: uppercase;
    white-space: nowrap; padding-top: 4px;
  }
  .step-body { flex: 1; display: flex; flex-direction: column; align-items: center; text-align: center; padding-top: 12px; }
  .step-lead {
    font-family: "Poppins", sans-serif; font-weight: 700;
    font-size: 24px; line-height: 26px; color: var(--navy);
  }
  .lead-rule { width: 72px; height: 3px; background: var(--navy); margin: 14px 0 8px; }
  .checklist { list-style: none; display: flex; flex-direction: column; width: 100%; }
  .checklist li {
    font-family: "Montserrat", sans-serif; font-weight: 500;
    font-size: 16.5px; line-height: 18px; color: var(--ink);
    display: flex; flex-direction: column; align-items: center;
  }
  .checklist li::before {
    content: "✓"; width: 17px; height: 17px; border-radius: 50%;
    background: var(--check); color: var(--white);
    font-size: 11px; line-height: 17px; font-weight: 700; margin-bottom: 3px;
  }
  .list-think { gap: 17px; padding: 0 50px; }
  .list-supports { gap: 7px; padding: 0 20px; }
  .list-ask { gap: 7px; padding: 0 14px; }
  .step-note {
    margin-top: 15px; width: 100%; background: var(--note);
    font-family: "Montserrat", sans-serif; font-weight: 500;
    font-size: 16.5px; line-height: 18px; color: var(--ink); padding: 7px 40px;
  }
  .step-foot {
    height: 72px; background: var(--yellow); border-radius: 0 0 30px 0;
    display: flex; align-items: center; justify-content: center; gap: 12px;
    font-family: "Poppins", sans-serif; font-weight: 800; font-size: 28px;
    color: var(--navy); letter-spacing: -0.5px;
  }
  .foot-icon { width: 24px; height: 24px; }

  .footer {
    position: absolute; left: 0; top: 1260px; width: 1000px; height: 155px;
    background: var(--white); display: flex; align-items: center;
  }
  .footer-name {
    font-family: "Arimo", Arial, sans-serif; font-weight: 700;
    font-size: 29px; line-height: 30px; color: #000; margin-left: 85px; width: 225px;
  }
  .footer-divider { width: 3px; height: 84px; background: #000; margin: 0 20px 0 0; }
  .references {
    font-family: "Poppins", sans-serif; font-weight: 600; font-size: 9.6px;
    line-height: 17px; color: var(--ink); text-transform: uppercase; margin-top: -14px;
  }
</style>
</head>
<body>
<main class="poster">
  <svg class="hero-art" viewBox="0 0 1000 600">
    <defs>
      <linearGradient id="photo-tone" x1="0" y1="0" x2="1" y2="1">
        <stop offset="0" stop-color="var(--photo-a)"/>
        <stop offset="1" stop-color="var(--photo-b)"/>
      </linearGradient>
    </defs>
    <polygon points="868,0 894,0 505,577 478,577" fill="var(--yellow)"/>
    <polygon role="img" aria-label="Photo of a smiling teacher with glasses holding books and gesturing toward the headline" points="894,0 1000,0 1000,577 505,577" fill="url(#photo-tone)"/>
  </svg>

  <header class="brand">
    <span class="brand-dot"></span>
    <span class="brand-name">Tolvane State<br>High School</span>
  </header>
  <div class="rule-top"></div>

  <h1 class="headline">Before you<br>ask the<br><span class="accent">teacher...</span></h1>
  <div class="rule-mid"></div>

  <h2 class="steps-banner">TRY THESE STEPS FIRST!</h2>

  <section class="steps">
    <article class="step step-think">
      <span class="step-num">1</span>
      <div class="step-head">
        <svg class="step-icon" viewBox="0 0 64 64" fill="none" stroke="var(--navy)" stroke-width="2" stroke-linejoin="round" stroke-linecap="round">
          <path d="M22 56v-9c-6-4-10-10-9-18 1-11 10-18 21-17 10 1 17 9 17 19l5 8-5 1v6c0 3-3 5-6 5h-5v5"/>
          <circle cx="32" cy="29" r="5"/>
          <path d="M32 19v4M32 35v4M22 29h4M38 29h4M25 22l3 3M36 33l3 3M39 22l-3 3M28 33l-3 3"/>
        </svg>
        <span class="step-divider"></span>
        <h3 class="step-title">Think<br>first</h3>
      </div>
      <div class="step-body">
        <p class="step-lead">Don't give up<br>straight away.</p>
        <span class="lead-rule"></span>
        <ul class="checklist list-think">
          <li>Read the question carefully.</li>
          <li>Identify what you already know.</li>
          <li>Try a strategy you've used before.</li>
          <li>Give yourself thinking time.</li>
        </ul>
      </div>
      <div class="step-foot">
        <svg class="foot-icon" viewBox="0 0 24 24"><polygon points="12,2 15,9 22,9.5 16.5,14 18.5,21.5 12,17.5 5.5,21.5 7.5,14 2,9.5 9,9" fill="var(--navy)"/></svg>
        WE BELIEVE
      </div>
    </article>

    <article class="step step-supports">
      <span class="step-num">2</span>
      <div class="step-head">
        <svg class="step-icon" viewBox="0 0 64 64" fill="none" stroke="var(--navy)" stroke-width="2" stroke-linejoin="round">
          <path d="M4 10h24l8 8v36H4z"/>
          <path d="M28 10v8h8M10 28h20M10 34h20M10 40h20M10 46h14"/>
          <path d="M44 14h10v34l-5 8-5-8z"/>
          <path d="M44 20h10M44 42h10"/>
        </svg>
        <span class="step-divider"></span>
        <h3 class="step-title">Check your<br>supports</h3>
      </div>
      <div class="step-body">
        <p class="step-lead">Before asking<br>for help, check:</p>
        <span class="lead-rule"></span>
        <ul class="checklist list-supports">
          <li>Learning goal and success criteria.</li>
          <li>Worked examples.</li>
          <li>Class notes.</li>
          <li>Classroom displays.</li>
          <li>Studyhub resources.</li>
          <li>Task sheet and instructions.</li>
        </ul>
      </div>
      <div class="step-foot">
        <svg class="foot-icon" viewBox="0 0 24 24" fill="var(--navy)"><path d="M6 3h12v6a6 6 0 0 1-12 0z"/><path d="M6 5H2v2a4 4 0 0 0 4 4M18 5h4v2a4 4 0 0 1-4 4" fill="none" stroke="var(--navy)" stroke-width="2"/><rect x="10.5" y="14" width="3" height="4"/><rect x="7" y="18" width="10" height="3"/></svg>
        WE STRIVE
      </div>
    </article>

    <article class="step step-ask">
      <span class="step-num">3</span>
      <div class="step-head">
        <svg class="step-icon" viewBox="0 0 64 64" fill="none" stroke="var(--navy)" stroke-width="2" stroke-linejoin="round">
          <path d="M24 6c-11 0-20 7-20 17 0 5 3 10 7 13l-3 8 10-5c2 1 4 1 6 1 11 0 20-8 20-17S35 6 24 6z"/>
          <path d="M46 24c8 2 14 8 14 16 0 4-2 8-5 11l3 7-9-4c-2 1-4 1-7 1-7 0-13-4-15-10"/>
          <text x="12" y="30" font-family="Poppins, sans-serif" font-size="18" font-weight="600" fill="var(--navy)" stroke="none">!?</text>
        </svg>
        <span class="step-divider"></span>
        <h3 class="step-title">Ask 3<br>before me</h3>
      </div>
      <div class="step-body">
        <p class="step-lead">Ask three sources<br>before asking the<br>teacher:</p>
        <span class="lead-rule"></span>
        <ul class="checklist list-ask">
          <li>A person<br>(partner or neighbour)</li>
          <li>A place<br>(notes, display, Studyhub)</li>
          <li>A resource<br>(worked example, task sheet)</li>
        </ul>
        <p class="step-note">Then ask the teacher if you still need help.</p>
      </div>
      <div class="step-foot">
        <svg class="foot-icon" viewBox="0 0 24 24" fill="var(--navy)"><polygon points="1,20 9,6 13,13 16,9 23,20"/></svg>
        WE ACHIEVE
      </div>
    </article>
  </section>

  <footer class="footer">
    <p class="footer-name">Tolvane State<br>High School</p>
    <span class="footer-divider"></span>
    <p class="references">
      Halloran, J. 2025, "Why students don't ask for help - and how to change that"<br>
      Downloaded on 24/04/2026 from https://www.learnwell.org/article/getting-students-ask-help/<br>
      ELRO, 2024. "Supporting self-regulated learning", downloaded on 24/04/2026 from
    </p>
  </footer>
</main>
</body>
</html>
```